Web Design Nutrition supplements (Quillstack 5 pages)

We are looking for templates for a new nutrition supplement shop www.velmorida.ch , targeting Swiss Female 65% /Male 35% over 40 yrs with high quality products (no performance enhancement /Body building products).
Our customers are not the most proficient in internet, so the website should be simple, easily understood. not too much web2.0 look and feel and functionality.

velmorida.ch product offerings are high quality and supplied from top brands: like Dr. Wentholm, Soravin, talbrücken, Nalvimed), for diets, weight management, antistress, anti-apathy, oligo-elements, omega-3 oils, and cosmetics.

We want the website design
1) to reflect our seriousness and expertise in the area,
2)to Inspire trust from our customers and address their needs in a personal and professional way (we answer your questions over email/Phone)
3) though we are not an pharmacy, our products are currently sold in pharmacies in Switzerland, so we want our customers to feel as well served online, as if they were in a pharmacy.
4) compare favorably to international websites (F, G) also selling online to Swiss customers: we are a truly Swiss company and can deliver within less than 18 h. in Switzerland (so the Swiss flag is an important design element for us)

We want to provide a superior buying experience,
1) important: providing sufficient product information: (intelligible snippet/summary of product info) should be visible on search result pages, and category pages,
2) clarity of design "emphasis" on products with clear call to action (buy)

Deliverables for the winning designer;
Photoshop files that can be easily be integrated in our quillstack shop.
- Homepage
- Category Page
- Product Page
For 1st evaluation and corrections of the proposals.

- Landing Page (for SEM Campaigns)
- Newsletter (Post raven)
as a second step.

Please use the attached wireframes, that should give you the exact content we want to provide (as well as functionality), the wireframes donnot define the user experience/design (it s more like a guidance, suggestion)

Target Market(s)

Swiss Males /35% Females 65% (both Swiss French/ Swiss German over 40 years

Industry/Entity Type

Nutrition

Requirements
Must have
• Deliverables:
- Homepage
- Category Page
- Product Page

- Newsletter template
- Landing Page

We attach:
- navigation to show how users can access the products (cat/ sub cat, but also search for body parts, objectives of healing... (see Kategorien-for-web.xls)
- Wireframes (myKrondelo)
- Logo (1 psd)
- Product images (zip files)
- Benchmarks: vitorelle.co.uk (simplicity), pmv.com (expandable navigation),
- Competitors: ko7.de, tramelo.com, tramelo-deutschland.de, quint-fold.eu

```html
<!DOCTYPE html>
<html lang="de">
<head>
<meta charset="utf-8">
<title>velmorida – Nahrungsergänzung</title>
<link rel="stylesheet" href="https://fonts.googleapis.com/css2?family=Roboto:ital,wght@0,400;0,500;0,700;1,400;1,700&family=Arvo:wght@700&family=Dosis:wght@400;500&display=swap">
<style>
:root{
  --bg:#e4e8eb;
  --topbar:#f3f4f5;
  --ink:#3a4650;
  --muted:#7d8890;
  --slate:#5a6f7c;
  --green:#6e9e12;
  --green-dark:#4f7a0b;
  --red:#d1302e;
  --blue:#2f77b5;
  --buy:#6fb62a;
  --magenta:#a3154f;
  --pink:#c8116a;
  --title-blue:#4a7fa5;
  --dark-band:#2d3d34;
  --footer:#d5dbe0;
  --white:#ffffff;
}
*{box-sizing:border-box;margin:0;padding:0}
html,body{width:1048px;height:1200px;overflow:hidden}
body{background:var(--bg);font-family:"Roboto",Arial,sans-serif;color:var(--ink);position:relative}
a{color:inherit;text-decoration:none}
.abs{position:absolute}

.topbar{position:absolute;left:0;top:0;width:1048px;height:37px;background:var(--topbar);border-bottom:2px dashed #d6dadd}
.topbar a{position:absolute;top:11px;font-size:11px;font-weight:500;color:var(--slate)}

.logo{position:absolute;left:116px;top:74px;display:flex;align-items:center;gap:8px}
.logo .mark{width:40px;height:40px;background:var(--green);border-radius:4px}
.logo .name{font-size:38px;font-weight:500;color:var(--slate);letter-spacing:-.5px}

.feature{position:absolute;display:flex;align-items:center;gap:8px;font-size:10.5px;font-weight:500;line-height:12px;color:var(--ink)}
.sep{position:absolute;top:56px;width:1px;height:44px;background:#cfd4d8}

.cart-label{position:absolute;left:811px;top:49px;font-size:11px;font-weight:700;color:var(--red)}
.cart{position:absolute;left:810px;top:66px;width:120px;height:31px;background:var(--white);border-radius:4px;display:flex;align-items:center;padding-left:6px;gap:6px;font-size:8.5px;font-weight:700;color:var(--red)}
.cart .ico{width:22px;height:20px;border:1px solid #cfd4d8;border-radius:3px;display:flex;align-items:center;justify-content:center}

.search{position:absolute;left:365px;top:111px;width:364px;height:28px;background:var(--white);border-radius:14px;border:1px solid #d2d7db}
.search svg{position:absolute;right:10px;top:5px}
.help{position:absolute;left:758px;top:116px;display:flex;align-items:center;gap:5px;font-size:11px;color:var(--slate)}
.lang{position:absolute;top:119px;display:flex;align-items:center;gap:4px;font-size:10px}

.nav{position:absolute;left:115px;top:168px;width:819px;height:41px;background:#f7f8f9;border:1px dashed #cfd5da;display:flex;align-items:center;padding-left:12px;font-size:10px;font-weight:500;color:var(--slate)}
.nav span.div{color:#b9c1c7;margin:0 6px}
.nav .active{color:var(--green)}

.dropdown{position:absolute;left:206px;top:215px;width:158px;height:147px;background:linear-gradient(#78a812,#5e8e0c);border-radius:3px;border-bottom:6px solid var(--dark-band);z-index:5}
.dropdown li{list-style:none;height:27px;display:flex;align-items:center;padding-left:9px;gap:8px;color:var(--white);font-size:9.5px;font-weight:500;border-bottom:1px solid rgba(255,255,255,.2)}
.dropdown li::before{content:"";width:4px;height:4px;border-radius:50%;background:var(--white)}
.dropdown li:last-child{border-bottom:none}

.hero{position:absolute;left:115px;top:229px;width:574px;height:261px;background:linear-gradient(90deg,#e9ecee,#f8f9fa 60%,#eef0f2);border:1px solid #d7dce0}
.hero .visual{position:absolute;left:16px;top:10px;width:262px;height:240px;background:linear-gradient(135deg,#f1e3ea,#f5f3f4 60%,#e6e3e6);border-radius:4px}
.hero h1{position:absolute;left:313px;top:56px;font-family:"Arvo",Georgia,serif;font-size:24px;line-height:30px;color:var(--title-blue)}
.hero h1 em{font-style:normal;color:var(--pink)}
.hero p{position:absolute;left:316px;top:123px;width:240px;font-size:9.5px;line-height:12px;color:#4c555c}
.hero .btn{position:absolute;left:315px;top:178px;width:100px;height:31px;background:var(--magenta);color:var(--white);font-size:10px;display:flex;align-items:center;padding-left:6px;gap:8px}
.hero .btn i{width:18px;height:18px;border-radius:50%;background:#e876a8;display:flex;align-items:center;justify-content:center}
.dots{position:absolute;left:525px;top:246px;display:flex;gap:5px}
.dots b{width:7px;height:7px;border-radius:50%;background:#c9ced2}
.dots b:first-child{background:#4c5358}

.support{position:absolute;left:712px;top:229px;width:222px;height:261px;background:linear-gradient(135deg,#c9d3db,#e8ecef 55%,#dfe4e8);overflow:hidden}
.support .person{position:absolute;left:0;top:60px;width:115px;height:201px;background:linear-gradient(180deg,#d8c8bb,#e9e6e4 55%,#cfd6dc)}
.support .corner{position:absolute;right:0;bottom:0;width:120px;height:70px;background:#3b4d59;clip-path:polygon(100% 0,100% 100%,0 100%)}
.support .call{position:absolute;left:20px;top:20px;font-size:14px;color:var(--ink)}
.support .call b{font-weight:700}
.support .big{position:absolute;left:137px;top:92px;font-size:30px;color:#3b474f}
.support .band{position:absolute;left:120px;top:122px;width:102px;height:23px;background:#3a4852;color:var(--white);font-size:17px;letter-spacing:1px;display:flex;align-items:center;justify-content:center}
.support .open{position:absolute;left:120px;top:156px;width:102px;text-align:center;font-size:11px;line-height:14px;color:#4c555c}

.promo{position:absolute;top:509px;width:265px;height:128px;overflow:hidden}
.promo .visual{position:absolute;left:0;top:0;width:107px;height:128px}
.promo .ribbon{position:absolute;left:-6px;top:-2px;width:105px;height:60px;background:#f2cf15;clip-path:polygon(0 60%,60% 0,100% 0,0 100%)}
.promo .off{position:absolute;left:5px;top:21px;transform:rotate(-40deg);font-size:12px;font-weight:700;color:#2b2b2b}
.promo .band{position:absolute;left:107px;top:13px;width:158px;height:36px;color:var(--white);font-size:11px;font-weight:500;display:flex;align-items:center;padding-left:11px}
.promo .desc{position:absolute;left:113px;top:54px;font-size:11px;font-style:italic;line-height:14px;color:#2b2b2b}
.promo .price{position:absolute;left:113px;top:87px;font-size:18px;font-weight:700;font-style:italic;color:#1f1f1f}
.promo .price em{color:#b0200e}
.promo .shop{position:absolute;left:183px;top:109px;width:82px;height:19px;background:#1f2521;color:var(--white);font-size:9px;font-style:italic;display:flex;align-items:center;justify-content:center;gap:4px}

.card{position:absolute;top:659px;width:142px;height:264px;background:var(--white);border:1px solid #dde1e4}
.card .visual{position:absolute;left:8px;top:8px;width:126px;height:122px;border-radius:3px}
.card h3{position:absolute;left:8px;top:140px;font-size:9.5px;font-weight:700;text-decoration:underline;color:var(--ink)}
.card .stars{position:absolute;left:9px;top:155px;font-size:10px;letter-spacing:1px;color:#e04646}
.card .stars i{font-style:normal;color:#c9cdd0}
.card p{position:absolute;left:10px;top:176px;font-size:8.5px;line-height:11px;color:#8a9298}
.card .price{position:absolute;left:12px;top:206px;font-size:11px;color:var(--red)}
.card .price s{font-size:8px;color:#9aa2a8;margin-right:4px}
.card .more{position:absolute;left:10px;top:227px;width:42px;height:25px;background:var(--blue);color:var(--white);font-size:11px;font-weight:700;display:flex;align-items:center;justify-content:center}
.card .buy{position:absolute;left:52px;top:227px;width:80px;height:25px;background:var(--buy);color:var(--white);font-size:11px;font-weight:700;display:flex;align-items:center;justify-content:center;gap:4px}

.footer{position:absolute;left:0;top:954px;width:1048px;height:189px;background:var(--footer);border-top:2px dashed #c3cad0}
.footer .links{position:absolute;left:124px;top:16px;font-size:9.5px;font-weight:500;color:var(--ink)}
.footer .links span{margin:0 8px;color:#667}
.footer .rule{position:absolute;left:115px;top:40px;width:819px;height:1px;background:#bfc7cd}
.col{position:absolute;top:60px}
.col h4{font-family:"Dosis",sans-serif;font-weight:500;font-size:17px;letter-spacing:.5px;color:var(--green);margin-bottom:5px}
.col li{list-style:none;width:108px;margin-left:9px;padding:2px 0 1px;border-bottom:1px dashed #a9b2b9;font-size:9.5px;color:#5a7088}
.badge{position:absolute}

.bottom{position:absolute;left:0;top:1143px;width:1048px;height:57px;background:#e8ebee}
.bottom .copy{position:absolute;left:127px;top:16px;font-size:9px;color:#5b656c}
.bottom .copy b{color:var(--ink);font-weight:500}
.bottom .accept{position:absolute;left:701px;top:17px;font-size:9.5px;font-weight:500;color:var(--ink)}
.pay{position:absolute;top:12px;width:34px;height:20px;border-radius:2px;color:var(--white);font-size:6.5px;font-weight:700;display:flex;align-items:center;justify-content:center}
</style>
</head>
<body>

<header class="topbar">
  <a style="left:766px">Melden Sie sich an</a>
  <a style="left:891px">Login</a>
</header>

<div class="logo"><span class="mark"></span><span class="name">velmorida</span></div>

<div class="feature" style="left:363px;top:64px">
  <svg width="26" height="26" viewBox="0 0 26 26"><circle cx="13" cy="14" r="10" fill="none" stroke="#e0453a" stroke-width="2.5"/><path d="M13 8v6l4 3" stroke="#e0453a" stroke-width="2" fill="none"/><path d="M3 6l4-3M23 6l-4-3" stroke="#e0453a" stroke-width="2.5"/></svg>
  <span>18 Std. Lieferung<br>in der Schweiz</span>
</div>
<div class="sep" style="left:496px"></div>
<div class="feature" style="left:508px;top:64px">
  <svg width="26" height="22" viewBox="0 0 26 22"><rect x="1" y="4" width="15" height="11" fill="#27495f"/><path d="M16 7h5l4 4v4h-9z" fill="#27495f"/><circle cx="6" cy="17" r="3" fill="#27495f" stroke="#fff"/><circle cx="20" cy="17" r="3" fill="#27495f" stroke="#fff"/></svg>
  <span>Gratisversand ab<br>80 CHF</span>
</div>
<div class="sep" style="left:638px"></div>
<div class="feature" style="left:649px;top:68px">
  <svg width="26" height="22" viewBox="0 0 26 22"><rect x="1" y="1" width="18" height="13" rx="3" fill="#5b9bc5"/><path d="M5 14l-1 6 6-6z" fill="#5b9bc5"/><rect x="10" y="7" width="15" height="11" rx="3" fill="#8ec13a"/></svg>
  <span>Experten Beratung</span>
</div>
<div class="sep" style="left:793px;top:52px"></div>

<div class="cart-label">Zum Warenkorb</div>
<div class="cart">
  <span class="ico"><svg width="14" height="12" viewBox="0 0 14 12"><path d="M1 4h12l-2 7H3z" fill="none" stroke="#4a555c" stroke-width="1.3"/><path d="M4 4l3-3 3 3" fill="none" stroke="#4a555c" stroke-width="1.3"/></svg></span>
  <span>0 Items - 0.00 CHF</span>
</div>

<div class="search">
  <svg width="18" height="18" viewBox="0 0 18 18"><circle cx="7.5" cy="7.5" r="5.5" fill="none" stroke="#d9352f" stroke-width="2.2"/><path d="M11.5 11.5l5 5" stroke="#d9352f" stroke-width="2.5"/></svg>
</div>
<div class="help">
  <svg width="20" height="20" viewBox="0 0 20 20"><circle cx="10" cy="10" r="9" fill="#fff" stroke="#3b88b8" stroke-width="2"/><text x="10" y="14.5" text-anchor="middle" font-size="12" font-weight="700" fill="#e0a51c" font-family="Arial">?</text></svg>
  <span>Help</span>
</div>
<div class="lang" style="left:834px">
  <svg width="20" height="14"><rect width="20" height="5" fill="#111"/><rect y="5" width="20" height="4" fill="#d9001b"/><rect y="9" width="20" height="5" fill="#f2c200"/></svg>
  <span style="color:#b7bdc2">DE</span>
</div>
<div class="lang" style="left:883px">
  <svg width="20" height="14"><rect width="7" height="14" fill="#1d3f9b"/><rect x="7" width="6" height="14" fill="#fff"/><rect x="13" width="7" height="14" fill="#e1251b"/></svg>
  <span style="color:#4a6f99;text-decoration:underline">FR</span>
</div>

<nav class="nav">
  <a>Vitamins Meneralien</a><span class="div">|</span>
  <a class="active">Essentielle Fettsäure</a><span class="div">|</span>
  <a>Prä- Probiotika</a><span class="div">|</span>
  <a>Spirulina-Maca</a><span class="div">|</span>
  <a>Gewichtsabnahme</a><span class="div">|</span>
  <a>Kosmetik</a><span class="div">|</span>
  <a>Phytotherapie</a><span class="div">|</span>
  <a>funktionelle Nahrung</a><span class="div">|</span>
  <a>ANGEBOTE</a>
</nav>

<ul class="dropdown">
  <li>Sub-Category 1</li><li>Sub-Category 2</li><li>Sub-Category 3</li><li>Sub-Category 4</li><li>Sub-Category 5</li>
</ul>

<section class="hero">
  <div class="visual" role="img" aria-label="Product boxes of a digestive supplement with a 20% discount sticker"></div>
  <h1>Lorem Ipsum Dolor<br><em style="color:var(--title-blue)">Sit</em> <em>Amet</em></h1>
  <p>Lorem ipsum dolor sit amet. This is just a sample text blurb with maximum of 3-4 sentences or Lines to make this area look perfect.</p>
  <a class="btn"><i><svg width="10" height="10" viewBox="0 0 10 10"><path d="M1 5h7M5 2l3 3-3 3" stroke="#a3154f" stroke-width="1.6" fill="none"/></svg></i>VIEW MORE</a>
  <div class="dots"><b></b><b></b><b></b><b></b></div>
</section>

<aside class="support">
  <div class="person" role="img" aria-label="Customer support agent wearing a headset"></div>
  <div class="corner"></div>
  <div class="call">Call us at: <b>(925) 418 3062</b></div>
  <div class="big">24x7</div>
  <div class="band">SUPPORT</div>
  <div class="open">We are open all the time for your help!</div>
</aside>

<article class="promo" style="left:113px;background:linear-gradient(90deg,#9fcf84,#b9d7a6 60%,#98be7f)">
  <div class="visual" role="img" aria-label="Jar of lemon balm base tablets" style="background:linear-gradient(160deg,#5d6fa3,#8fc07a 55%,#c9e0b5)"></div>
  <div class="ribbon"></div><div class="off">15% OFF</div>
  <div class="band" style="background:#2f3b33">MELISSEN-BASENTABLETT</div>
  <div class="desc">Lorem ipsum dolor sit<br>amet. Small desc...</div>
  <div class="price">Only at <em>300 CHF</em></div>
  <a class="shop">SHOP NOW →</a>
</article>
<article class="promo" style="left:391px;background:linear-gradient(90deg,#f0b98c,#f4c9a4 60%,#eeb17f)">
  <div class="visual" role="img" aria-label="Supplement bottle with vitamin complex" style="background:linear-gradient(160deg,#e9dfcf,#f1e9dd 55%,#e6a66f)"></div>
  <div class="ribbon"></div><div class="off">10% OFF</div>
  <div class="band" style="background:#8a3208">VENATUR</div>
  <div class="desc">Lorem ipsum dolor sit<br>amet. Small desc...</div>
  <div class="price">Only at <em>250 CHF</em></div>
  <a class="shop">SHOP NOW →</a>
</article>
<article class="promo" style="left:667px;background:linear-gradient(90deg,#a9c9e6,#c4dbef 60%,#9fc2e2)">
  <div class="visual" role="img" aria-label="Tin of alkaline mineral powder" style="background:linear-gradient(160deg,#8ab4dc,#e9f1f8 55%,#3d6aa5)"></div>
  <div class="ribbon"></div><div class="off">25% OFF</div>
  <div class="band" style="background:#0f4a97">BASENPULVER</div>
  <div class="desc">Lorem ipsum dolor sit<br>amet. Small desc...</div>
  <div class="price">Only at <em>300 CHF</em></div>
  <a class="shop">SHOP NOW →</a>
</article>

<article class="card" style="left:118px">
  <div class="visual" role="img" aria-label="Product box of a chocolate flavoured supplement" style="background:linear-gradient(135deg,#2f5ea3,#e9edf2 55%,#d9a24c)"></div>
  <h3>Corvelle Chocolat All</h3>
  <div class="stars">★★★★★</div>
  <p>Lorem ipsum dolor sit amet.<br>Small description ...</p>
  <div class="price"><s>240 CHF</s>200 CHF</div>
  <a class="more">More</a><a class="buy">🛒 Buy Now</a>
</article>
<article class="card" style="left:283px">
  <div class="visual" role="img" aria-label="Product box of a digestive supplement" style="background:linear-gradient(135deg,#c51a6a,#f3eef1 45%,#e6e2e4)"></div>
  <h3>Dolveniane</h3>
  <div class="stars">★★★★★</div>
  <p>Lorem ipsum dolor sit amet.<br>Small description ...</p>
  <div class="price"><s>240 CHF</s>200 CHF</div>
  <a class="more">More</a><a class="buy">🛒 Buy Now</a>
</article>
<article class="card" style="left:451px">
  <div class="visual" role="img" aria-label="White jar of a mineral supplement" style="background:linear-gradient(135deg,#f0f1f2,#e7d4c8 55%,#ececec)"></div>
  <h3>K Morane</h3>
  <div class="stars">★★★★★</div>
  <p>Lorem ipsum dolor sit amet.<br>Small description ...</p>
  <div class="price"><s>240 CHF</s>200 CHF</div>
  <a class="more">More</a><a class="buy">🛒 Buy Now</a>
</article>
<article class="card" style="left:622px">
  <div class="visual" role="img" aria-label="Slim tube of a mineral salt supplement" style="background:linear-gradient(135deg,#f2f4f5,#bfe1e0 50%,#f2f4f5)"></div>
  <h3>K-salin</h3>
  <div class="stars">★★★★<i>★</i></div>
  <p>Lorem ipsum dolor sit amet.<br>Small description ...</p>
  <div class="price"><s>240 CHF</s>200 CHF</div>
  <a class="more">More</a><a class="buy">🛒 Buy Now</a>
</article>
<article class="card" style="left:788px">
  <div class="visual" role="img" aria-label="Product box of a fermented nutrition supplement" style="background:linear-gradient(135deg,#3e88c2,#e8f0f5 50%,#9cc43a)"></div>
  <h3>Fervalune Nutrition Active</h3>
  <div class="stars">★★★★<i>★</i></div>
  <p>Lorem ipsum dolor sit amet.<br>Small description ...</p>
  <div class="price"><s>240 CHF</s>200 CHF</div>
  <a class="more">More</a><a class="buy">🛒 Buy Now</a>
</article>

<footer class="footer">
  <div class="links">Impressum<span>|</span>Wer sind Wir?<span>|</span>Uber uns<span>|</span>AGB's</div>
  <div class="rule"></div>
  <div class="col" style="left:124px"><h4>KUNDENSERVICE</h4><ul><li>Kontact</li><li>Lexikon</li><li>Hilfe &amp; Antworten</li><li>Blog</li><li>Partnerprogramm</li><li>Reseller Programm</li></ul></div>
  <div class="col" style="left:300px"><h4>NAVIGATIONHILFE</h4><ul><li>Suchbegiffe</li><li>Marken</li><li>Erweiterte Suche</li><li>Sitemap</li></ul></div>
  <div class="col" style="left:477px"><h4>Das Unternehmen</h4><ul><li>Expertise</li><li>Jobs</li><li>User Team</li></ul></div>
  <div class="badge" style="left:658px;top:86px;width:68px;height:45px;background:#f6cf0f;border:1px solid #d0ad10"></div>
  <div class="badge" style="left:739px;top:90px;width:77px;height:36px;background:#eef0f2;border:2px solid #b22a3a;border-radius:18px"></div>
  <div class="badge" style="left:829px;top:80px;width:54px;height:54px;background:#3c4248;border-radius:50%"></div>
  <div class="badge" style="left:872px;top:91px;width:60px;height:32px;background:#23282c;border-radius:4px"></div>
</footer>

<div class="bottom">
  <div class="copy">© 2012 <b>velmorida</b>. All Rights Reserved.</div>
  <div class="accept">We Accept:</div>
  <div class="pay" style="left:762px;background:#1d4f9c">PAVO</div>
  <div class="pay" style="left:806px;background:#1d4f9c">PAVO E</div>
  <div class="pay" style="left:847px;background:#2b3a67">MERITA</div>
  <div class="pay" style="left:888px;background:#2e6aa8">CIRVO</div>
</div>

</body>
</html>
```